Plumbing distributor looking for flyer to advertise new product line

We are looking for a flyer to advertise a new product line we are carrying. We are plumbing wholesale distributor that sells to plumbing and fire sprinkler contractors. We are expanding our product line to sell fire pump repair parts (Link to Plexo on what a fire pump is https://en.plexopedia.net/wiki/Fire_pump)
We are wanting a flyer have the manufacturers logos we are carrying parts for as well as talking about our technical assistance and same day shipping.
The product types we will be carrying are
Fire Pump repack kits
Fast Packs
Case Gaskets
Packing
Gland Bolt Assemblies
Lantern Rings
Bearings
Jockey Pumps

If you want to find other images you can google any of the fire pump manufacture names with "fire pump" to find other images

Our website is www.rivetquayspares.com

Industry/Entity Type

Wholesale

Colors

Designer to choose colors to be used in the design.

Requirements
Must have
• Be targeted to businesses not retail

```html
<!DOCTYPE html>
<html lang="en">
<head>
<meta charset="utf-8">
<title>Fire Pump Repair Parts Flyer</title>
<link href="https://fonts.googleapis.com/css2?family=Archivo+Black&family=Open+Sans:wght@400;600;700;800&display=swap" rel="stylesheet">
<style>
  :root {
    --blue: #2f4fa6;
    --blue-dark: #223c86;
    --red: #e8194c;
    --red-pump: #c8232c;
    --white: #ffffff;
    --grey-light: #f2f3f5;
    --grey-mid: #c9ccd1;
    --ink: #2b2b2b;
    --logo-ink: #4a5160;
    --stage: #ececec;
  }
  * { box-sizing: border-box; margin: 0; padding: 0; }
  html, body { width: 1200px; height: 848px; overflow: hidden; background: var(--stage); }
  .flyer {
    position: absolute; left: 300px; top: 0; width: 600px; height: 848px;
    background: linear-gradient(180deg, var(--white) 0%, var(--grey-light) 40%, var(--grey-mid) 100%);
    overflow: hidden; font-family: "Open Sans", sans-serif; color: var(--ink);
  }
  .header-band { position: absolute; left: 0; top: 0; width: 600px; height: 240px; }
  .title { position: absolute; left: 30px; top: 26px; color: var(--white); font-family: "Archivo Black", sans-serif; line-height: 1; }
  .title-main { display: block; font-size: 78px; letter-spacing: 2px; }
  .title-sub { display: block; font-size: 38px; letter-spacing: 3px; margin-top: 8px; }
  .badge {
    position: absolute; left: 468px; top: 118px; width: 116px; height: 116px; border-radius: 50%;
    background: var(--red); border: 3px solid var(--white);
    display: flex; align-items: center; justify-content: center; text-align: center;
    color: var(--white); font-weight: 700; font-size: 11px; line-height: 1.25; padding: 14px; z-index: 3;
  }
  .intro { position: absolute; left: 30px; top: 230px; width: 280px; }
  .intro-heading { color: var(--red); font-size: 22px; font-weight: 800; font-style: italic; margin-bottom: 6px; }
  .intro-text { font-size: 12px; line-height: 1.4; font-weight: 600; }
  .pump-photo {
    position: absolute; left: 316px; top: 226px; width: 250px; height: 150px; border-radius: 6px;
    background: radial-gradient(ellipse at 50% 45%, #e03a3e 0%, var(--red-pump) 55%, #8e1a20 100%); z-index: 2;
  }
  .product { position: absolute; width: 170px; height: 104px; background: var(--white); box-shadow: 0 2px 5px rgba(0,0,0,.15); }
  .product-photo { position: absolute; left: 8px; top: 6px; right: 8px; height: 70px; border-radius: 3px; }
  .product-label {
    position: absolute; left: 0; right: 0; bottom: 0; height: 22px; background: var(--red);
    color: var(--white); font-size: 11px; font-weight: 700; text-align: center; line-height: 22px; white-space: nowrap;
  }
  .tone-tan { background: linear-gradient(135deg, #d9c6a0, #8a7a60); }
  .tone-steel { background: linear-gradient(135deg, #e3e6ea, #8d949e); }
  .tone-red { background: linear-gradient(135deg, #d64040, #7a2a2a); }
  .tone-pale { background: linear-gradient(135deg, #e9efe9, #a9b6ad); }
  .tone-dark { background: linear-gradient(135deg, #7a7a7a, #1e1e1e); }
  .maker-list {
    position: absolute; left: 24px; top: 636px; width: 184px; list-style: none;
    display: grid; grid-template-columns: 88px 88px; gap: 12px 8px;
  }
  .maker { font-size: 11.5px; font-weight: 700; color: var(--logo-ink); display: flex; align-items: center; gap: 5px; white-space: nowrap; }
  .maker-dot { width: 8px; height: 8px; background: var(--logo-ink); border-radius: 50%; flex: none; }
  .company { position: absolute; left: 24px; top: 744px; color: var(--blue); line-height: 1.05; }
  .company-name { font-size: 22px; font-weight: 400; }
  .company-sub { font-size: 12px; font-weight: 400; }
  .footer {
    position: absolute; left: 0; top: 790px; width: 600px; height: 58px; background: var(--red);
    color: var(--white); text-align: center; padding-top: 9px; font-size: 13px; font-weight: 600; line-height: 1.45;
  }
</style>
</head>
<body>
<main class="flyer">
  <svg class="header-band" viewBox="0 0 600 240" aria-hidden="true">
    <path d="M0 0 H600 V150 C450 205 240 230 0 215 Z" fill="var(--blue)"/>
    <path d="M0 215 C240 230 450 205 600 150 V162 C450 218 240 242 0 228 Z" fill="var(--blue-dark)" opacity=".35"/>
  </svg>

  <h1 class="title">
    <span class="title-main">FIRE PUMP</span>
    <span class="title-sub">REPAIR PARTS</span>
  </h1>

  <div class="badge">Well As Talking About Our Technical Assistance And Same Day Shipping.</div>

  <section class="intro">
    <h2 class="intro-heading">Same Day Shipping</h2>
    <p class="intro-text">We use fast, reliable and insured shipping couriers to get your backflow parts to you, on time – every time anywhere in the country or around the world. We guarantee same day shipping and our website even provides ParcelPath tracking so you'll know where your order is and when it will arrive.</p>
  </section>

  <div class="pump-photo" role="img" aria-label="Red split-case fire pump on a steel base"></div>

  <div class="product" style="left:24px;top:406px">
    <div class="product-photo tone-tan" role="img" aria-label="Fire pump repack kit with packing and O-rings"></div>
    <div class="product-label">Fire Pump repack kits</div>
  </div>
  <div class="product" style="left:24px;top:518px">
    <div class="product-photo tone-steel" role="img" aria-label="Gland bolt assembly"></div>
    <div class="product-label">Gland Bolt Assemblies</div>
  </div>

  <div class="product" style="left:215px;top:406px">
    <div class="product-photo tone-red" role="img" aria-label="Fast pack pump component"></div>
    <div class="product-label">Fast Packs</div>
  </div>
  <div class="product" style="left:215px;top:518px">
    <div class="product-photo tone-pale" role="img" aria-label="Lantern rings"></div>
    <div class="product-label">Lantern Rings</div>
  </div>
  <div class="product" style="left:215px;top:630px">
    <div class="product-photo tone-steel" role="img" aria-label="Ball bearing"></div>
    <div class="product-label">Bearings</div>
  </div>

  <div class="product" style="left:406px;top:428px">
    <div class="product-photo tone-steel" role="img" aria-label="Case gasket"></div>
    <div class="product-label">Case Gaskets</div>
  </div>
  <div class="product" style="left:406px;top:540px">
    <div class="product-photo tone-dark" role="img" aria-label="Coiled pump packing"></div>
    <div class="product-label">Packing</div>
  </div>
  <div class="product" style="left:406px;top:652px">
    <div class="product-photo tone-red" role="img" aria-label="Vertical jockey pumps"></div>
    <div class="product-label">Jockey Pumps</div>
  </div>

  <ul class="maker-list" aria-label="Manufacturers we carry parts for">
    <li class="maker"><span class="maker-dot"></span>Northvale</li>
    <li class="maker"><span class="maker-dot"></span>Keswick</li>
    <li class="maker"><span class="maker-dot"></span>Brightwater</li>
    <li class="maker"><span class="maker-dot"></span>Corran Pump</li>
    <li class="maker"><span class="maker-dot"></span>Halbrook</li>
    <li class="maker"><span class="maker-dot"></span>Tamsin</li>
    <li class="maker"><span class="maker-dot"></span>Ardmore</li>
  </ul>

  <div class="company">
    <div class="company-name">Rivet Quay Spares</div>
    <div class="company-sub">Products Company</div>
  </div>

  <footer class="footer">
    <div>412 Harbor Mill Road, Portwell, FL 32000</div>
    <div>Phone: (800) 555-0147 | Fax: (850) 555-0162 | www.rivetquayspares.com</div>
  </footer>
</main>
</body>
</html>
```